Birch and Bough Tree Services Business Card Design

We need a business card design for our company based in Melbourne, Australia. We are a tree services business. We already have a logo designed by a designer on craft hive, so obviously we would like this to be incorporated in to the design, including similar colours. The final design should be sleek.

It should have:

Marcus Whitfield
Chief Executive Officer

www.quillhollowarbor.com.au
marcus.whitfield@quillhollowarbor.com.au
0491 736 208

Industry/Entity Type

Business

```html
<!DOCTYPE html>
<html lang="en">
<head>
<meta charset="utf-8">
<title>Birch and Bough Tree Services – Business Card</title>
<link rel="stylesheet" href="https://fonts.googleapis.com/css2?family=Open+Sans:wght@400;600&display=swap">
<style>
  :root {
    --bg: #242424;
    --white: #ffffff;
    --lime: #8cf000;
    --lime-pale: #f3fbe2;
    --lime-glow: #ffffff;
    --ink: #141414;
    --ink-soft: #2e2e2e;
    --muted: #4d6b12;
  }
  * { box-sizing: border-box; margin: 0; padding: 0; }
  html, body {
    width: 1200px; height: 1077px; overflow: hidden;
    background: var(--bg);
    font-family: "Open Sans", Arial, sans-serif;
  }
  .stage { position: relative; width: 1200px; height: 1077px; }

  .card { position: absolute; top: 384px; height: 309px; overflow: hidden; }

  .card-front-logo {
    left: 48px; width: 281px; background: var(--white);
    display: flex; flex-direction: column; align-items: center; justify-content: center; gap: 22px;
  }
  .card-back-details {
    left: 335px; width: 257px; background: var(--lime);
    padding: 30px 16px 0 14px; text-align: right; color: var(--ink);
  }
  .card-wide-logo {
    left: 625px; width: 545px;
    background: radial-gradient(ellipse at 50% 45%, var(--lime-glow) 0%, var(--lime-pale) 70%, #e6f5c6 100%);
    display: flex; flex-direction: column; align-items: center; justify-content: center; gap: 30px;
  }

  .brand-mark { border-radius: 50%; background: var(--lime); }
  .card-front-logo .brand-mark { width: 110px; height: 110px; }
  .card-wide-logo .brand-mark { width: 150px; height: 150px; }

  .brand-name {
    color: var(--ink); font-weight: 400; text-align: center; line-height: 1.2;
  }
  .card-front-logo .brand-name { font-size: 20px; }
  .card-wide-logo .brand-name { font-size: 28px; }

  .person-name { font-size: 22px; font-weight: 400; line-height: 1.1; white-space: nowrap; }
  .person-role { font-size: 9px; color: var(--muted); margin-top: 3px; }
  .address { font-size: 9px; line-height: 1.5; margin-top: 32px; color: var(--ink-soft); }

  .contact-list { list-style: none; margin-top: 56px; font-size: 9px; color: var(--ink-soft); }
  .contact-list li {
    display: flex; justify-content: flex-end; align-items: center; gap: 8px; height: 19px;
    white-space: nowrap;
  }
  .contact-list svg { width: 10px; height: 10px; flex: none; }
</style>
</head>
<body>
<main class="stage">

  <section class="card card-front-logo">
    <div class="brand-mark"></div>
    <p class="brand-name">Birch and Bough<br>Tree Services</p>
  </section>

  <section class="card card-back-details">
    <h1 class="person-name">Marcus Whitfield</h1>
    <p class="person-role">Chief Executive Officer</p>
    <p class="address">27 Fernlea Road<br>Melbourne VIC 3000</p>
    <ul class="contact-list">
      <li>0491 736 208
        <svg viewBox="0 0 12 12"><rect x="3" y="0.5" width="6" height="11" rx="1.2" fill="var(--ink)"/><rect x="4" y="2" width="4" height="6" fill="var(--lime)"/></svg>
      </li>
      <li>03 9416 2075
        <svg viewBox="0 0 12 12"><rect x="0.5" y="4" width="11" height="7" rx="1" fill="var(--ink)"/><rect x="3" y="1" width="6" height="4" fill="var(--ink)"/></svg>
      </li>
      <li>marcus.whitfield@quillhollowarbor.com.au
        <svg viewBox="0 0 12 12"><rect x="0.5" y="2" width="11" height="8" rx="1" fill="var(--ink)"/><path d="M1 3 L6 7 L11 3" stroke="var(--lime)" stroke-width="1" fill="none"/></svg>
      </li>
      <li>www.quillhollowarbor.com.au
        <svg viewBox="0 0 12 12"><circle cx="6" cy="6" r="5.5" fill="var(--ink)"/><path d="M0.5 6 H11.5 M6 0.5 V11.5" stroke="var(--lime)" stroke-width="0.8"/><ellipse cx="6" cy="6" rx="2.5" ry="5.5" stroke="var(--lime)" stroke-width="0.8" fill="none"/></svg>
      </li>
    </ul>
  </section>

  <section class="card card-wide-logo">
    <div class="brand-mark"></div>
    <p class="brand-name">Birch and Bough<br>Tree Services</p>
  </section>

</main>
</body>
</html>
```